Coffee Promotion for Specialty Coffees

I need to have a poster designed to promote our coffee sales. We offer cappuccino for $3.75, Latte for $3.75, Americano for $2.00, Espresso $2.00 and Fair Trade Organic Colombian Coffee for $1.75 Med, $2.00L Large. I would like sometihng very visual that shows the coffees and also has the pricing, and includes the wording" Try our Amazing Specialty Coffees!" Our logo is attached as well

Poster size is 24" wide x 36" high

Target Market(s)

Seniors and Students in a Mall Setting

Colors

Designer to choose colors to be used in the design.

Requirements
Must have
• Graphic artwork of coffees (cappuccinos, lattes, etc). Logo included in artwork. Must be for 24"wide x 36" high poster
Nice to have
• Would like something that shows closeups of the coffees and visually sells the coffee being premium and delicious.

```html
<!DOCTYPE html>
<html lang="en">
<head>
<meta charset="utf-8">
<title>Swirlhouse Specialty Coffees Poster</title>
<link href="https://fonts.googleapis.com/css2?family=Lobster&family=Lobster+Two:ital,wght@1,700&family=Quicksand:wght@600&display=swap" rel="stylesheet">
<style>
  :root {
    --backdrop: #e9eaec;
    --night: #15191d;
    --navy: #1a2530;
    --smoke-top: #5a5756;
    --smoke-bottom: #26272b;
    --gold: #d9ae4e;
    --cream: #ffffff;
    --roast: #7a4428;
    --roast-deep: #3b1d10;
  }
  * { margin: 0; padding: 0; box-sizing: border-box; }
  html, body { width: 841px; height: 1200px; overflow: hidden; background: var(--backdrop); }
  .poster {
    position: absolute; left: 20px; top: 0; width: 800px; height: 1200px;
    background: var(--night); overflow: hidden;
  }
  .band-feature {
    position: absolute; left: 0; top: 230px; width: 800px; height: 405px;
    background: radial-gradient(ellipse at 45% 20%, var(--smoke-top), var(--smoke-bottom) 75%);
  }
  .band-menu {
    position: absolute; left: 0; top: 635px; width: 800px; height: 434px;
    background: linear-gradient(180deg, var(--navy), #141b22);
  }
  .band-footer {
    position: absolute; left: 0; top: 1069px; width: 800px; height: 131px;
    background: linear-gradient(180deg, #1f2b36, var(--navy));
  }
  .tear { position: absolute; left: 0; width: 800px; height: 20px; }
  .bean-photo {
    position: absolute; left: 4px; top: 471px; width: 420px; height: 172px;
    background: radial-gradient(ellipse at 50% 50%, rgba(91,77,67,0.9), rgba(58,50,46,0.6) 55%, rgba(58,50,46,0) 72%);
  }
  .cup-photo {
    position: absolute; left: 473px; top: 200px; width: 327px; height: 500px;
    background: radial-gradient(ellipse 75% 60% at 75% 45%, var(--roast) 0%, #5a2f1a 50%, rgba(59,29,16,0.85) 75%, rgba(59,29,16,0) 100%);
  }
  .brand {
    position: absolute; left: 271px; top: 41px; width: 258px; height: 258px;
    border-radius: 50%; background: var(--night); border: 3px solid var(--cream);
    display: flex; align-items: center; justify-content: center;
    font-family: "Lobster", cursive; font-size: 44px; color: var(--cream);
  }
  .headline { position: absolute; left: 46px; top: 277px; color: var(--gold); font-weight: normal; }
  .headline-lead {
    font-family: "Quicksand", sans-serif; font-weight: 600; font-size: 24px;
    line-height: 28px; letter-spacing: 2.4px;
  }
  .headline-main {
    font-family: "Lobster Two", cursive; font-weight: 700; font-style: italic;
    font-size: 97px; line-height: 82px;
  }
  .headline-main span { display: block; white-space: nowrap; }
  .headline-main .second { padding-left: 124px; }
  .menu { position: absolute; left: 107px; top: 744px; width: 580px; list-style: none; }
  .menu-item {
    display: flex; align-items: center; height: 57px;
    font-family: "Lobster", cursive; font-size: 46px; color: var(--cream);
  }
  .cup-icon { width: 47px; height: 30px; margin-right: 21px; flex: none; }
  .menu-name { flex: none; }
  .leader { flex: 1; height: 3px; background: var(--cream); margin: 18px 12px 0 6px; }
  .price { flex: none; width: 96px; white-space: nowrap; }
  .footer-note {
    position: absolute; left: 0; top: 1083px; width: 800px; text-align: center;
    font-family: "Lobster", cursive; font-size: 33px; line-height: 40px; color: var(--gold);
  }
</style>
</head>
<body>
<main class="poster">
  <div class="band-feature"></div>
  <div class="band-menu"></div>
  <div class="band-footer"></div>

  <svg class="tear" style="top:222px" viewBox="0 0 800 20" preserveAspectRatio="none">
    <polyline fill="none" stroke="#ffffff" stroke-width="3" points="0,12 30,6 55,11 80,4 110,10 140,5 170,12 200,7 230,11 260,4 300,10 330,6 360,12 400,8 430,4 470,10 500,6 530,12 570,5 600,10 640,6 680,11 720,4 760,9 800,6"/>
  </svg>
  <div class="bean-photo" role="img" aria-label="Close-up photo of a roasted coffee bean"></div>
  <svg class="tear" style="top:626px" viewBox="0 0 800 20" preserveAspectRatio="none">
    <polyline fill="none" stroke="#ffffff" stroke-width="3" points="0,8 35,14 60,6 95,12 130,5 160,13 195,7 225,12 260,5 290,11 330,6 360,13 395,7 430,12 470,6 500,13 540,8 580,12 620,15"/>
  </svg>
  <div class="cup-photo" role="img" aria-label="Photo of an espresso cup on a saucer with coffee beans"></div>
  <svg class="tear" style="top:1060px" viewBox="0 0 800 20" preserveAspectRatio="none">
    <polyline fill="none" stroke="#d9ae4e" stroke-width="4" points="0,12 40,7 70,12 110,5 150,11 190,6 230,12 270,4 310,10 350,6 390,12 430,5 470,11 510,7 550,12 590,4 630,10 670,6 710,12 750,5 800,9"/>
  </svg>

  <div class="brand">Swirlhouse</div>

  <h1 class="headline">
    <div class="headline-lead">Try our Amazing</div>
    <div class="headline-main"><span>specialty</span><span class="second">Coffees!</span></div>
  </h1>

  <ul class="menu">
    <li class="menu-item">
      <svg class="cup-icon" viewBox="0 0 48 30"><path d="M10 4h22v10a11 11 0 0 1-22 0z" fill="#fff"/><path d="M32 7h4a4 4 0 0 1 0 8h-4" fill="none" stroke="#fff" stroke-width="2.5"/><rect x="1" y="25" width="46" height="3" rx="1.5" fill="#fff"/></svg>
      <span class="menu-name">Cappuccino</span><span class="leader"></span><span class="price">$3.75</span>
    </li>
    <li class="menu-item">
      <svg class="cup-icon" viewBox="0 0 48 30"><path d="M10 4h22v10a11 11 0 0 1-22 0z" fill="#fff"/><path d="M32 7h4a4 4 0 0 1 0 8h-4" fill="none" stroke="#fff" stroke-width="2.5"/><rect x="1" y="25" width="46" height="3" rx="1.5" fill="#fff"/></svg>
      <span class="menu-name">Latte</span><span class="leader" style="margin-left:36px"></span><span class="price">$3.75</span>
    </li>
    <li class="menu-item">
      <svg class="cup-icon" viewBox="0 0 48 30"><path d="M10 4h22v10a11 11 0 0 1-22 0z" fill="#fff"/><path d="M32 7h4a4 4 0 0 1 0 8h-4" fill="none" stroke="#fff" stroke-width="2.5"/><rect x="1" y="25" width="46" height="3" rx="1.5" fill="#fff"/></svg>
      <span class="menu-name">Americano</span><span class="leader"></span><span class="price">$2.00</span>
    </li>
    <li class="menu-item">
      <svg class="cup-icon" viewBox="0 0 48 30"><path d="M10 4h22v10a11 11 0 0 1-22 0z" fill="#fff"/><path d="M32 7h4a4 4 0 0 1 0 8h-4" fill="none" stroke="#fff" stroke-width="2.5"/><rect x="1" y="25" width="46" height="3" rx="1.5" fill="#fff"/></svg>
      <span class="menu-name">Espresso</span><span class="leader"></span><span class="price">$2.00</span>
    </li>
  </ul>

  <p class="footer-note">Fair Trade Organic Colombian<br>Coffee for $1.75 | Med $2.00L Large.</p>
</main>
</body>
</html>
```